IT support company needs Banner Ad for the top of their quote layout template

We need a banner Ad for the top of our for quote layout template so it is sent out on all our quotes

The banner size must be 827 x 100 pixels - anything larger than 60 KB can cause upload time issues

We have attached our logo and examples of the quote page to see how it looks in the context of the whole page.

Essential elements of the banner
- Must have our logo but this can be changed to be different colours if it makes the design work better i.e. Tidal Ember could be all in white

Colours
- Can use all of our standard colours - Orange, Black, Grey and White

Images
- As a premium IT support company we deal with people and technology so would like to see both of these Incorporated into the banner i.e. people using technology These images could be watermarked or one colour effect.

Look and Feel
- Professional, friendly, people, technology, premium

Target Market
Small business owners and managers

Industry/Entity Type

It Company

```html
<!DOCTYPE html>
<html lang="nl">
<head>
<meta charset="utf-8">
<title>Offerte DJ-000280</title>
<link rel="stylesheet" href="https://fonts.googleapis.com/css2?family=Open+Sans:wght@400;600;700&display=swap">
<style>
  :root{
    --orange:#f26f21;
    --orange-soft:#f29a6e;
    --orange-pale:#f7b48f;
    --ink:#1a1a1a;
    --grey:#e9eaec;
    --row-alt:#f3f3f3;
    --white:#ffffff;
  }
  *{box-sizing:border-box;margin:0;padding:0}
  html,body{width:899px;height:1200px;overflow:hidden;background:var(--white)}
  body{font-family:"Open Sans",Arial,sans-serif;color:var(--ink);font-size:12.5px;position:relative}
  .abs{position:absolute}

  /* banner */
  .banner{left:0;top:0;width:899px;height:105px;background:var(--grey);overflow:hidden}
  .banner-rule{left:0;top:107px;width:899px;height:5px;background:var(--orange-pale)}
  .brand{left:34px;top:33px;font-size:31px;font-weight:700;letter-spacing:0.5px;color:var(--ink);display:flex;align-items:center;gap:10px}
  .brand-dot{width:14px;height:14px;border-radius:50%;background:var(--orange)}
  .banner-shape{left:300px;top:0}
  .tagline{left:400px;top:28px;width:226px;text-align:center;color:var(--white);font-weight:600;font-size:13.5px;line-height:18.5px;letter-spacing:0.2px}
  .banner-photo{left:690px;top:0;width:209px;height:105px;background:linear-gradient(90deg,rgba(233,234,236,1) 0%,#dfe3ea 25%,#c9d3e0 60%,#eef1f5 100%)}

  /* header block */
  .doc-title{left:29px;top:170px;font-size:19.5px;font-weight:400}
  .headshot{left:27px;top:210px;width:107px;height:133px;background:linear-gradient(180deg,#8a8a8a,#3d3d3d)}
  .col h3{font-size:15.5px;font-weight:400;color:var(--orange);margin-bottom:4px}
  .col p{line-height:18px}
  .col strong{font-weight:700}
  .col-from{left:146px;top:206px}
  .col-to{left:391px;top:206px}
  .col-meta{left:682px;top:206px}
  .rule{left:27px;top:356px;width:844px;height:3px;background:var(--orange)}

  .section-title{font-size:17.5px;font-weight:400;left:29px}

  /* tables */
  .quote-table{border-collapse:collapse;border:1.5px solid var(--ink);width:844px;left:27px}
  .quote-table th{height:26px;font-weight:400;text-align:left;padding:0 6px;
    background:linear-gradient(90deg,var(--orange-soft),var(--white) 50%,var(--orange-soft))}
  .quote-table th.num{background:var(--orange-soft)}
  .quote-table td{height:27px;padding:0 6px}
  .quote-table tbody tr:nth-child(even) td{background:var(--row-alt)}
  .quote-table .num{text-align:right;border-left:1.5px solid var(--ink)}
  .quote-table .w-amt{width:117px}
  .quote-table .w-rec{width:119px}

  .totals{right:36px;display:grid;grid-template-columns:auto 98px;row-gap:8px;text-align:right}
  .totals dt{color:var(--orange)}
  .totals dd{font-weight:700}

  .disclaimer{left:29px;top:1008px}
  .sign{top:1082px;border-top:1.5px solid var(--ink);padding-top:3px}
  .sign-name{left:27px;width:504px}
  .sign-date{left:563px;width:199px}

  .footer-rule{left:0;top:1155px;width:899px;height:5px;background:var(--orange-pale)}
  .footer{left:0;top:1162px;width:899px;height:38px;display:flex;justify-content:space-between;align-items:center;padding:0 30px;
    background:linear-gradient(90deg,var(--white),var(--orange-soft) 50%,var(--white))}
</style>
</head>
<body>

<header>
  <div class="abs banner"></div>
  <div class="abs brand"><span>TIDAL EMBER</span><span class="brand-dot"></span></div>
  <svg class="abs banner-shape" width="420" height="105" viewBox="0 0 420 105" aria-hidden="true">
    <polygon points="90,8 102,8 8,105 -4,105" fill="#1a1a1a"/>
    <polygon points="100,8 382,8 290,105 14,105" fill="#f26f21"/>
    <polygon points="388,0 396,0 300,105 292,105" fill="#1a1a1a"/>
  </svg>
  <div class="abs tagline">BRINGING ENTERPRISE-LEVEL SOLUTIONS TO EAST ANGLIA SMALL BUSINESSES</div>
  <div class="abs banner-photo" role="img" aria-label="Foto van een man die aan een bureau op een laptop werkt"></div>
  <div class="abs banner-rule"></div>
</header>

<main>
  <h1 class="abs doc-title">Standard MSP&nbsp;&nbsp;#2</h1>
  <div class="abs headshot" role="img" aria-label="Portretfoto van de opsteller"></div>

  <section class="abs col col-from">
    <h3>Opgesteld door:</h3>
    <p><strong>Harlow Reed Ltd</strong></p>
    <p>Harlow Reed</p>
    <p>&nbsp;</p>
    <p>Fax</p>
    <p>harlow.reed@quotemail.example</p>
  </section>
  <section class="abs col col-to">
    <h3>Opgesteld voor:</h3>
    <p><strong>Copper Vale</strong></p>
    <p>218 Linden Rd.</p>
    <p>Ashford,&nbsp;&nbsp; 40312</p>
    <p>Nora Whitfield</p>
    <p>nora.whitfield@bluefinch.example</p>
  </section>
  <section class="abs col col-meta">
    <h3>Gegevens Offerte:</h3>
    <p><strong>Offerte #: DJ-000280</strong></p>
    <p>Versie: 1</p>
    <p>Leverdatum: 14/11/2017</p>
    <p>Vervaldatum: 31/12/2017</p>
  </section>
  <div class="abs rule"></div>

  <h2 class="abs section-title" style="top:382px">Overzicht Offerte</h2>
  <table class="abs quote-table" style="top:413px">
    <thead><tr><th>Beschrijving</th><th class="num w-amt">Bedrag</th></tr></thead>
    <tbody><tr><td>Initial Investment</td><td class="num">$800.00</td></tr></tbody>
  </table>
  <dl class="abs totals" style="top:473px">
    <dt>Subtotaal:</dt><dd>$800.00</dd>
    <dt>VAT:</dt><dd>$160.00</dd>
    <dt>Totaal:</dt><dd>$960.00</dd>
  </dl>

  <h2 class="abs section-title" style="top:563px">Overzicht Terugkerende Kosten</h2>
  <table class="abs quote-table" style="top:591px">
    <thead><tr><th>Beschrijving</th><th class="num w-amt">Bedrag</th></tr></thead>
    <tbody>
      <tr><td>Monitoring</td><td class="num">$375.00</td></tr>
      <tr><td>Support</td><td class="num">$65.00</td></tr>
      <tr><td>Fixed Hours</td><td class="num">$850.00</td></tr>
    </tbody>
  </table>
  <dl class="abs totals" style="top:705px">
    <dt>Terugkerende totaal:</dt><dd>$1,290.00</dd>
  </dl>

  <h2 class="abs section-title" style="top:757px">*Optionele kosten</h2>
  <table class="abs quote-table" style="top:787px">
    <thead><tr><th>Beschrijving</th><th class="num w-rec">Recurring</th><th class="num w-amt">One-Time</th></tr></thead>
    <tbody>
      <tr><td>Monitoring</td><td class="num">$790.00</td><td class="num">$0.00</td></tr>
      <tr><td>Support</td><td class="num">$185.00</td><td class="num">$0.00</td></tr>
      <tr><td>Fixed Hours</td><td class="num">$695.00</td><td class="num">$0.00</td></tr>
      <tr><td>Add-on Services</td><td class="num">$850.00</td><td class="num">$0.00</td></tr>
    </tbody>
  </table>
  <dl class="abs totals" style="top:927px">
    <dt>Optionele terugkerend bedrag:</dt><dd>$2,520.00</dd>
    <dt>Optionele ongeplande Subtotaal:</dt><dd>$.00</dd>
  </dl>

  <p class="abs disclaimer">Taxes, shipping, handling and other fees may apply.&nbsp; We reserve the right to cancel orders arising from pricing or other errors.</p>

  <div class="abs sign sign-name">Handtekening</div>
  <div class="abs sign sign-date">Datum</div>
</main>

<div class="abs footer-rule"></div>
<footer class="abs footer">
  <span>Offerte #DJ-000280 v1</span>
  <span>Pagina 6 Van 7</span>
</footer>

</body>
</html>
```